Off Grid consulting and outdoor products needs a website

We need a website design to help launch our new business. Its a business that plans to offer Off-grid conslting and outdoor survival products to people who are looking to relocate or vacation to properties/homes that are Off-grid. We plan to offer design plans for homes/cabins, renewable energy systems for power/heating etc, survival products for outdoor vacations/living. We also do consulting and project management for those who want to design and build from scratch their dream off-grid home or vacation property. I've included our logo design for use.
Would like the website to include 5 pages.
www.ridgepinehaven.com
The main landing page (1)
want a video loop backround with a flyover of a cabin in the woods.
https://www.clipvaultora.com/video/clip-48291736-blue-sky-melting-snow-on-green-energy
(also need a backup static image of just high-shot of cabin in woods)
logo top left, Quoted string of text in the middle, over the video. and a CTA button to 'Contact us'
picture links below that to last 3 recent blog posts.
About Us page (2)
(example) https://larkwildgear.com/pages/about-lark
Blog page (3)
blog posts associated with pictures.
Consulting 'services' page (4)
-land services and moving off-grid
-Building off grid
-Renewable energy off-grid
-Sustainable farming and all season greenhouses
Store page 'comming soon' (5)
(Example) http://timberly.crestlayouts.com/demo-1/demo.html

Target Market(s)

Outdoor enthusiasts and people who want to escape their city life

Coding

Coded - Design and coding required

Requirements
Must have
• Outdoor feel, woods, cabin, reneable energy (solar, geothermal, greenhouses, water wells)

```html
<!DOCTYPE html>
<html lang="en">
<head>
<meta charset="utf-8">
<title>Ridgepine Haven — Off Grid Living</title>
<link href="https://fonts.googleapis.com/css2?family=Anton&family=Lato:wght@400;700&family=Poppins:wght@400;500&family=Roboto:wght@400;500&display=swap" rel="stylesheet">
<style>
:root{
  --ink:#0b0f0b;
  --forest:#0f1c12;
  --moss:#5d7160;
  --moss-dark:#4d6250;
  --paper:#ffffff;
  --muted:#6f6f6f;
  --line:#5a5a5a;
  --field:#ffffff;
}
*{box-sizing:border-box;margin:0;padding:0}
html,body{width:1200px;height:3057px;overflow:hidden}
body{font-family:'Lato',sans-serif;color:var(--ink);background:var(--paper);position:relative}
a{color:inherit;text-decoration:none}

/* Header */
.site-header{position:absolute;top:0;left:0;width:1200px;height:100px;background:var(--paper);z-index:3}
.main-nav{position:absolute;left:110px;top:38px;display:flex;gap:40px;font-size:16px;color:#333}
.main-nav .active{text-decoration:underline;color:#111}
.brand-badge{position:absolute;left:515px;top:-30px;width:172px;height:172px;border-radius:50%;background:var(--paper);display:flex;align-items:center;justify-content:center;padding-top:30px}
.brand-badge span{font-family:'Anton',sans-serif;font-size:24px;line-height:1.05;text-align:center;color:var(--ink);text-transform:uppercase}
.header-call{position:absolute;left:714px;top:40px;font-size:15px;font-family:'Roboto',sans-serif;display:flex;align-items:center;gap:10px}
.header-call b{font-weight:500}
.header-search{position:absolute;left:937px;top:41px}
.btn-contact{position:absolute;left:982px;top:25px;width:106px;height:46px;background:var(--ink);color:#fff;border-radius:5px;font-family:'Anton',sans-serif;font-size:16px;display:flex;align-items:center;justify-content:center}

/* Hero */
.hero{position:absolute;top:100px;left:0;width:1200px;height:600px;background:linear-gradient(180deg,#8fb4d9 0%,#c9d8e6 28%,#b8bfbf 42%,#6d7a70 60%,#3b4a3d 100%);text-align:center}
.hero-title{position:absolute;top:108px;width:100%;font-family:'Anton',sans-serif;color:var(--ink);text-transform:uppercase}
.hero-title .small{display:block;font-size:56px;line-height:1}
.hero-title .big{display:block;font-size:84px;line-height:1;margin-top:28px}
.hero-actions{position:absolute;top:307px;left:500px;display:flex;align-items:center;gap:32px}
.btn-outline{width:116px;height:48px;border:3px solid var(--ink);border-radius:6px;font-family:'Anton',sans-serif;font-size:16px;display:flex;align-items:center;justify-content:center}
.play{width:54px;height:54px;border-radius:50%;background:var(--forest);display:flex;align-items:center;justify-content:center}
.hero-arrow{position:absolute;top:278px}

/* Section headings */
.section-title{font-family:'Anton',sans-serif;font-size:32px;text-transform:uppercase;letter-spacing:.3px}

/* Blog */
.blog{position:absolute;top:700px;left:0;width:1200px;height:769px;text-align:center}
.blog .section-title{position:absolute;top:78px;width:100%}
.blog .lead{position:absolute;top:131px;width:100%;color:var(--muted);font-size:15px}
.cards{position:absolute;top:203px;left:111px;display:flex;gap:23px}
.card{width:310px;height:480px;background:#fff;box-shadow:0 2px 10px rgba(0,0,0,.12);border-bottom:4px solid var(--line);text-align:left}
.card-img{height:214px}
.card-body{padding:30px 28px 0}
.card-date{font-size:14px;color:var(--muted);display:flex;align-items:center;gap:9px}
.card-title{font-family:'Poppins',sans-serif;font-weight:400;font-size:19px;line-height:28px;margin-top:14px;color:#111}
.card-text{font-size:15px;line-height:26px;color:var(--muted);margin-top:12px;text-align:justify}
.card-link{display:inline-block;margin-top:12px;font-family:'Poppins',sans-serif;font-weight:500;font-size:15px;text-decoration:underline}

/* About */
.about{position:absolute;top:1469px;left:0;width:1200px;height:557px;background:var(--moss);color:#fff}
.about .section-title{position:absolute;top:100px;left:110px}
.about-text{position:absolute;top:168px;left:110px;width:437px;font-size:15px;line-height:26px;text-align:justify}
.btn-light{position:absolute;top:404px;left:111px;width:115px;height:48px;border:2px solid #fff;border-radius:6px;font-family:'Anton',sans-serif;font-size:16px;display:flex;align-items:center;justify-content:center}
.about-img{position:absolute;top:105px;left:605px;width:475px;height:340px;border-radius:40px;background:linear-gradient(120deg,#4b6a45,#8a5a3a 60%,#6e7d66)}

/* Contact */
.contact{position:absolute;top:2026px;left:0;width:1200px;height:694px;text-align:center}
.contact-bg{position:absolute;left:0;top:430px;width:1200px;height:264px;background:linear-gradient(180deg,#f4f5f3 0%,#bfc7bd 35%,#4f6550 75%,var(--forest) 100%)}
.contact .section-title{position:absolute;top:96px;width:100%}
.contact-form{position:absolute;top:174px;left:263px;width:673px;display:grid;grid-template-columns:330px 330px;gap:14px 13px}
.field{height:62px;background:var(--field);border-radius:4px;box-shadow:0 1px 6px rgba(0,0,0,.1);font-family:'Roboto',sans-serif;font-size:15px;color:#333;padding:22px 20px;text-align:left}
.field.message{grid-column:1/3;height:107px}
.btn-submit{position:absolute;top:469px;left:542px;width:116px;height:49px;background:var(--ink);color:#fff;border-radius:6px;font-family:'Anton',sans-serif;font-size:16px;display:flex;align-items:center;justify-content:center}

/* Footer */
.site-footer{position:absolute;top:2720px;left:0;width:1200px;height:337px;background:var(--forest);color:#fff;font-family:'Roboto',sans-serif}
.footer-brand{position:absolute;left:115px;top:60px;font-family:'Anton',sans-serif;font-size:44px;line-height:1.05;text-transform:uppercase}
.footer-col{position:absolute;top:45px}
.footer-col h4{font-weight:500;font-size:18px;letter-spacing:.3px;margin-bottom:18px}
.footer-col li{list-style:none;font-size:15px;line-height:26px}
.footer-col li::before{content:"» ";}
.contact-line{display:flex;gap:12px;font-size:15px;line-height:25px;margin-bottom:14px}
.newsletter{display:flex;margin-top:2px}
.newsletter .input{width:180px;height:44px;background:#fff;color:#777;font-size:15px;padding:12px;border-radius:3px 0 0 3px}
.newsletter .send{width:56px;height:44px;background:#6f7a70;display:flex;align-items:center;justify-content:center;border-radius:0 3px 3px 0}
.social{display:flex;gap:15px;margin-top:36px}
.social span{width:45px;height:45px;border:2px solid #fff;border-radius:50%}
.social span.filled{background:#6f7a70;border-color:#6f7a70}
.copyright{position:absolute;top:274px;width:100%;text-align:center;font-size:15px}
</style>
</head>
<body>

<header class="site-header">
  <nav class="main-nav">
    <a class="active" href="#">Home</a><a href="#">About</a><a href="#">Blog</a><a href="#">Services</a><a href="#">Store</a>
  </nav>
  <div class="brand-badge"><span>Ridgepine<br>Haven</span></div>
  <div class="header-call">
    <svg width="15" height="15" viewBox="0 0 24 24"><path fill="#111" d="M6.6 10.8a15.1 15.1 0 006.6 6.6l2.2-2.2c.3-.3.7-.4 1-.2 1.1.4 2.3.6 3.6.6.6 0 1 .4 1 1V20c0 .6-.4 1-1 1A17 17 0 013 4c0-.6.4-1 1-1h3.5c.6 0 1 .4 1 1 0 1.3.2 2.5.6 3.6.1.3 0 .7-.2 1z"/></svg>
    <span><b>Call :</b> +1(888) 888 8888</span>
  </div>
  <svg class="header-search" width="17" height="17" viewBox="0 0 24 24"><circle cx="10" cy="10" r="7" fill="none" stroke="#111" stroke-width="3"/><path d="M15 15l6 6" stroke="#111" stroke-width="3.5" stroke-linecap="round"/></svg>
  <a class="btn-contact" href="#">Contact us</a>
</header>

<section class="hero" role="img" aria-label="Aerial flyover of a snowy forest valley with an off-grid cabin and solar roof">
  <h1 class="hero-title"><span class="small">Welcome to</span><span class="big">Ridgepine Haven</span></h1>
  <div class="hero-actions">
    <a class="btn-outline" href="#">Get Started</a>
    <span class="play"><svg width="18" height="20" viewBox="0 0 18 20"><path d="M2 1l15 9-15 9z" fill="#fff"/></svg></span>
  </div>
  <svg class="hero-arrow" style="left:75px" width="24" height="44" viewBox="0 0 24 44"><path d="M21 3L4 22l17 19" fill="none" stroke="#111" stroke-width="4"/></svg>
  <svg class="hero-arrow" style="left:1101px" width="24" height="44" viewBox="0 0 24 44"><path d="M3 3l17 19L3 41" fill="none" stroke="#111" stroke-width="4"/></svg>
</section>

<section class="blog">
  <h2 class="section-title">Recent Blog</h2>
  <p class="lead">Sed ut perspiciatis unde omnis iste natus error sit voluptatem</p>
  <div class="cards">
    <article class="card">
      <div class="card-img" role="img" aria-label="Log cabin among tall pine trees" style="background:linear-gradient(160deg,#c9ccc6,#3f5a34 45%,#6b4a30)"></div>
      <div class="card-body">
        <p class="card-date"><svg width="15" height="15" viewBox="0 0 16 16"><circle cx="8" cy="8" r="6.5" fill="none" stroke="#777" stroke-width="1.8"/><path d="M8 4v4l-2 2" stroke="#777" stroke-width="1.8" fill="none"/></svg>April 13,2022</p>
        <h3 class="card-title">Sed ut perspiciatis unde omnis iste natus error sit</h3>
        <p class="card-text">Lorem ipsum dolor sit amet, elit, seddo eiusmod tempor incididunt ut labore et dolore magna aliqua.</p>
        <a class="card-link" href="#">Learn More</a>
      </div>
    </article>
    <article class="card">
      <div class="card-img" role="img" aria-label="Wooden lakeside cabin at golden hour" style="background:linear-gradient(170deg,#4d6b3a,#b8722e 50%,#3a2a14)"></div>
      <div class="card-body">
        <p class="card-date"><svg width="15" height="15" viewBox="0 0 16 16"><circle cx="8" cy="8" r="6.5" fill="none" stroke="#777" stroke-width="1.8"/><path d="M8 4v4l-2 2" stroke="#777" stroke-width="1.8" fill="none"/></svg>April 13,2022</p>
        <h3 class="card-title">Sed ut perspiciatis unde omnis iste natus error sit</h3>
        <p class="card-text">Lorem ipsum dolor sit amet, elit, seddo eiusmod tempor incididunt ut labore et dolore magna aliqua.</p>
        <a class="card-link" href="#">Learn More</a>
      </div>
    </article>
    <article class="card">
      <div class="card-img" role="img" aria-label="Aerial view of a cabin in a forest clearing by a lake" style="background:linear-gradient(180deg,#2f6f95,#3b7aa0 30%,#4e7a2c 60%,#2d4f20)"></div>
      <div class="card-body">
        <p class="card-date"><svg width="15" height="15" viewBox="0 0 16 16"><circle cx="8" cy="8" r="6.5" fill="none" stroke="#777" stroke-width="1.8"/><path d="M8 4v4l-2 2" stroke="#777" stroke-width="1.8" fill="none"/></svg>April 13,2022</p>
        <h3 class="card-title">Sed ut perspiciatis unde omnis iste natus error sit</h3>
        <p class="card-text">Lorem ipsum dolor sit amet, elit, seddo eiusmod tempor incididunt ut labore et dolore magna aliqua.</p>
        <a class="card-link" href="#">Learn More</a>
      </div>
    </article>
  </div>
</section>

<section class="about">
  <h2 class="section-title">About Ridgepine Haven</h2>
  <p class="about-text">Lorem ipsum dolor sit amet, consectetur adipiscing elit, sed do eiusmod tempor incididunt ut labore et dolore magna aliqua. Ut enim ad minim veniam, quis nostrud exercitation ullamco laboris nisi ut aliquip ex ea commodo consequat. Duis aute irure dolor in reprehenderit in voluptate velit esse cillum dolore eu fugiat nulla pariatur. Excepteur sint occaecat cupidatat non proident, sunt in culpa qui officia deserunt mollit anim id est laborum.</p>
  <a class="btn-light" href="#">Learn More</a>
  <div class="about-img" role="img" aria-label="Wooden cabin with a deck surrounded by forest"></div>
</section>

<section class="contact">
  <div class="contact-bg" role="img" aria-label="Misty pine forest treeline"></div>
  <h2 class="section-title">Contact Us</h2>
  <form class="contact-form">
    <div class="field">First Name</div>
    <div class="field">Last Name</div>
    <div class="field">Phone Number</div>
    <div class="field">Email Address</div>
    <div class="field message">Message</div>
  </form>
  <a class="btn-submit" href="#">Submit</a>
</section>

<footer class="site-footer">
  <div class="footer-brand">Ridgepine<br>Haven</div>
  <div class="footer-col" style="left:401px">
    <h4>QUICK LINKS</h4>
    <ul><li>Home</li><li>About</li><li>Blog</li><li>Services</li><li>Store</li></ul>
  </div>
  <div class="footer-col" style="left:582px">
    <h4>CONTACT US</h4>
    <div class="contact-line"><svg width="16" height="20" viewBox="0 0 16 22"><path d="M8 0a8 8 0 00-8 8c0 6 8 14 8 14s8-8 8-14a8 8 0 00-8-8zm0 11a3 3 0 110-6 3 3 0 010 6z" fill="#fff"/></svg><span>Lorem ipsum dolor sit<br>amet, consectetur</span></div>
    <div class="contact-line"><svg width="17" height="17" viewBox="0 0 24 24"><path fill="#fff" d="M6.6 10.8a15.1 15.1 0 006.6 6.6l2.2-2.2c.3-.3.7-.4 1-.2 1.1.4 2.3.6 3.6.6.6 0 1 .4 1 1V20c0 .6-.4 1-1 1A17 17 0 013 4c0-.6.4-1 1-1h3.5c.6 0 1 .4 1 1 0 1.3.2 2.5.6 3.6.1.3 0 .7-.2 1z"/></svg><span>+1 (888) 888 8888</span></div>
    <div class="contact-line"><svg width="17" height="14" viewBox="0 0 20 16"><rect width="20" height="16" rx="2" fill="#fff"/><path d="M1 2l9 7 9-7" stroke="#0f1c12" stroke-width="1.8" fill="none"/></svg><span>info@ridgepinehaven.com</span></div>
  </div>
  <div class="footer-col" style="left:852px">
    <h4>SIGN UP FOR NEWSLETTER</h4>
    <div class="newsletter"><div class="input">Email Address</div><div class="send"><svg width="18" height="14" viewBox="0 0 20 16"><rect width="20" height="16" rx="2" fill="#fff"/><path d="M1 2l9 7 9-7" stroke="#6f7a70" stroke-width="1.8" fill="none"/></svg></div></div>
    <div class="social" aria-label="Social links"><span></span><span class="filled"></span><span></span><span></span></div>
  </div>
  <p class="copyright">©Copyrights 2022 Ridgepinehaven &nbsp;| &nbsp; All Rights Reserved</p>
</footer>

</body>
</html>
```